Business card design for Velvet Harbor

We need business cards designed for our new marketing consulting company, Velvet Harbor. Our services include marketing strategy, go-to-market and launch planning, growth strategy, and execution. We serve medical technology and health technology companies, from startups to well-established growth companies.

The business cards should feel professional, credible, reliable and trustworthy, and should instill confidence. Also bold, creative, and modern.

The design must use the Velvet Harbor logo.

The primary brand color is this orange: #FF5501
A secondary color that you can use is this gray: #282B2D
I would prefer only to use the orange and gray. But if you feel you really need an additional accent color (please use it very sparingly, as little as possible), you can use this blue for small accent purposes: #009FED

Attached are the logo files. The main logo is the one with a little bit of orange on the left and the rest is gray.

The business card should include the following:

Velvet Harbor logo
First name and last name
Title
Email address
Phone number and type (in whatever order looks best for the design
Website (the website does not need to be in the same block as the personal info)

For example:

Nessa Pryle
Founder & Principal
nessa@velvetharbor.com
+1.628.309.4156 mobile (can use "." or spaces in between blocks of numbers)
velvetharbor.com (somewhere on the card, it does not need to be with the personal info; and note that there is no "www." at the beginning)

Note that there will be no address listed on the business card.

Target Market(s)

Executives (CEO, head of marketing, head of sales) at medical technology and health technology companies, mostly in their 40s and older, well-educated, often with advanced degrees. They are strategic thinkers, responsible for budgets, and familiar with P&L. Their comfort with and trust in using outside consultants varies.

Industry/Entity Type

Medical technology and health technology companies.

Contact Information for Business Card

See project description

Font styles to use
Sans Serif

Requirements
Must have
• Logo and see Business card details section above.

```html
<!DOCTYPE html>
<html lang="en">
<head>
<meta charset="utf-8">
<title>Velvet Harbor — Business Card</title>
<link href="https://fonts.googleapis.com/css2?family=Jost:wght@400;500;600&display=swap" rel="stylesheet">
<style>
  :root {
    --orange: #FF5501;
    --accent-orange: #e2531d;
    --gray: #282B2D;
    --text-gray: #3a3c3e;
    --rule: #8a8c8e;
    --card: #f7f7f7;
    --card-edge: #e9e9e9;
    --backdrop: #2f3133;
  }
  * { box-sizing: border-box; margin: 0; padding: 0; }
  html, body {
    width: 1200px;
    height: 900px;
    overflow: hidden;
  }
  body {
    background: var(--backdrop);
    font-family: "Jost", sans-serif;
    display: flex;
    flex-direction: column;
    align-items: center;
    justify-content: center;
    gap: 40px;
  }
  .card {
    position: relative;
    width: 700px;
    height: 400px;
    border-radius: 34px;
    background: linear-gradient(135deg, var(--card-edge) 0%, var(--card) 45%, #ffffff 100%);
    overflow: hidden;
  }

  /* Brand lockup: plain circle + wordmark */
  .brand {
    position: absolute;
    display: flex;
    align-items: center;
    gap: 22px;
  }
  .brand-dot {
    width: 70px;
    height: 70px;
    border-radius: 50%;
    background: var(--gray);
    flex: none;
  }
  .brand-name {
    font-family: "Jost", sans-serif;
    font-weight: 500;
    color: var(--gray);
    text-transform: uppercase;
    font-size: 40px;
    line-height: 0.98;
    letter-spacing: 0.2em;
  }

  /* Front */
  .card-front .website {
    position: absolute;
    left: 160px;
    top: 128px;
    font-size: 17px;
    font-weight: 500;
    color: var(--accent-orange);
    letter-spacing: 0.02em;
  }
  .card-front .brand { left: 64px; top: 160px; }

  /* Back */
  .card-back .brand { left: 64px; top: 70px; }
  .contact {
    position: absolute;
    left: 64px;
    bottom: 62px;
    width: 560px;
  }
  .contact-header {
    display: flex;
    align-items: baseline;
    gap: 12px;
    padding-bottom: 10px;
    border-bottom: 1px solid var(--rule);
  }
  .person-name {
    font-size: 30px;
    font-weight: 600;
    color: var(--accent-orange);
    text-transform: uppercase;
    letter-spacing: 0.01em;
  }
  .divider-bar {
    font-size: 30px;
    font-weight: 500;
    color: var(--accent-orange);
  }
  .person-title {
    font-size: 22px;
    font-weight: 400;
    color: var(--text-gray);
    letter-spacing: 0.02em;
  }
  .contact-lines {
    display: flex;
    align-items: center;
    gap: 10px;
    padding-top: 12px;
    font-size: 20px;
    color: var(--text-gray);
  }
  .contact-icon {
    width: 20px;
    height: 20px;
    flex: none;
  }
  .contact-sep { color: var(--text-gray); }
</style>
</head>
<body>

  <section class="card card-front" aria-label="Business card front">
    <p class="website">velvetharbor.com</p>
    <div class="brand">
      <span class="brand-dot"></span>
      <p class="brand-name">Velvet<br>Harbor</p>
    </div>
  </section>

  <section class="card card-back" aria-label="Business card back">
    <div class="brand">
      <span class="brand-dot"></span>
      <p class="brand-name">Velvet<br>Harbor</p>
    </div>

    <div class="contact">
      <div class="contact-header">
        <span class="person-name">Nessa Pryle</span>
        <span class="divider-bar">|</span>
        <span class="person-title">Founder &amp; Principal</span>
      </div>
      <div class="contact-lines">
        <svg class="contact-icon" viewBox="0 0 24 24" aria-hidden="true">
          <path fill="var(--accent-orange)" d="M6.6 10.8c1.4 2.8 3.8 5.1 6.6 6.6l2.2-2.2c.3-.3.7-.4 1-.2 1.1.4 2.3.6 3.6.6.6 0 1 .4 1 1V20c0 .6-.4 1-1 1C10.6 21 3 13.4 3 4c0-.6.4-1 1-1h3.5c.6 0 1 .4 1 1 0 1.3.2 2.5.6 3.6.1.3 0 .7-.2 1z"/>
        </svg>
        <span class="phone">+1.628.309.4156</span>
        <span class="contact-sep">|</span>
        <svg class="contact-icon" viewBox="0 0 24 24" aria-hidden="true">
          <rect x="2" y="5" width="20" height="14" rx="1.5" fill="var(--accent-orange)"/>
          <path d="M3 6.5l9 6.5 9-6.5" fill="none" stroke="#fff" stroke-width="1.6"/>
        </svg>
        <span class="email">nessa@velvetharbor.com</span>
      </div>
    </div>
  </section>

</body>
</html>
```